Copperleaf Motorized Shade Business Card

Hello, we've had our logo made. Now we are looking for a clean and cool looking business card. One side can just be the logo with any design elements that might look good with it. The other side will be Name, Phone Number and Email. There will not be an address on the card.

```html
<!DOCTYPE html>
<html lang="en">
<head>
<meta charset="utf-8">
<title>Copperleaf Motorized Shade – Business Card</title>
<link rel="stylesheet" href="https://fonts.googleapis.com/css2?family=Saira+Semi+Condensed:wght@400;500;600&display=swap">
<style>
  :root {
    --paper: #ffffff;
    --sun-edge: #fbbd2a;
    --sun-mid: #fdd46e;
    --sun-glow: #fff8e6;
    --ink: #2b3a63;
  }
  * { margin: 0; padding: 0; box-sizing: border-box; }
  html, body {
    width: 841px;
    height: 1200px;
    overflow: hidden;
    background: var(--paper);
  }
  .sheet {
    position: relative;
    width: 841px;
    height: 1200px;
    font-family: "Saira Semi Condensed", sans-serif;
    color: var(--ink);
  }
  .card {
    position: absolute;
    left: 3px;
    width: 835px;
    height: 540px;
  }
  .card--front {
    top: 3px;
    background: radial-gradient(ellipse 62% 72% at 52% 34%, var(--sun-glow) 0%, var(--sun-mid) 48%, var(--sun-edge) 100%);
  }
  .card--back {
    top: 657px;
    background: radial-gradient(ellipse 70% 80% at 58% 60%, #fee4a4 0%, var(--sun-mid) 55%, var(--sun-edge) 100%);
  }
  .trim-mark {
    position: absolute;
    width: 29px;
    height: 29px;
    background: var(--paper);
    border: 1px solid var(--sun-edge);
  }
  .trim-mark--tl { left: -3px; top: -3px; }
  .trim-mark--tr { right: -3px; top: -3px; }
  .trim-mark--bl { left: -3px; bottom: -3px; }
  .trim-mark--br { right: -3px; bottom: -3px; }

  .brand-name {
    position: absolute;
    left: 0;
    right: 0;
    top: 245px;
    text-align: center;
    font-weight: 600;
    font-size: 44px;
    line-height: 1;
    letter-spacing: 1px;
    color: var(--ink);
  }

  .contact {
    position: absolute;
    font-weight: 400;
    line-height: 1;
    white-space: nowrap;
    color: var(--ink);
  }
  .contact--name  { left: 96px;  top: 100px; font-size: 50px; }
  .contact--phone { left: 247px; top: 236px; font-size: 40px; }
  .contact--email { right: 96px; top: 358px; font-size: 40px; }
</style>
</head>
<body>
  <main class="sheet">
    <section class="card card--front" aria-label="Card front">
      <span class="trim-mark trim-mark--tl"></span>
      <span class="trim-mark trim-mark--tr"></span>
      <span class="trim-mark trim-mark--bl"></span>
      <span class="trim-mark trim-mark--br"></span>
      <p class="brand-name">Copperleaf Motorized Shade</p>
    </section>

    <section class="card card--back" aria-label="Card back">
      <span class="trim-mark trim-mark--tl"></span>
      <span class="trim-mark trim-mark--tr"></span>
      <span class="trim-mark trim-mark--bl"></span>
      <span class="trim-mark trim-mark--br"></span>
      <p class="contact contact--name">Name:COPPERLEAF</p>
      <p class="contact contact--phone">+977 9814276305</p>
      <p class="contact contact--email">Copperleaf@info.com</p>
    </section>
  </main>
</body>
</html>
```